Buch-/eBook-Cover für Frauen zwischen 16-35
Zielgruppe
MLT/ Mellow Lantern Typesetting. Ich suche Unterstützung für die Erstellung eines Buchcovers für Frauen zwischen 16-35.
Aufgabenstellung
Ich habe eine Zusammenfassung des Projektes in dem beigefügten Word Dokument zusammen mit Beispielcovern, Covern der Konkurrenz etc.

```html
<!DOCTYPE html>
<html lang="de">
<head>
<meta charset="utf-8">
<title>Das kleine Mutproben-Buch für beste Freundinnen – Cover</title>
<link rel="stylesheet" href="https://fonts.googleapis.com/css2?family=Marcellus&family=Sacramento&display=swap">
<style>
  :root {
    --backdrop: #ece4d9;
    --teal: #4a7a7b;
    --cream: #f6ecd9;
    --photo-warm: #d9a98e;
    --photo-glow: #f0d2b5;
    --photo-sea: #9c8a86;
    --sand: #c49a7c;
    --shadow: rgba(60, 40, 30, 0.18);
  }
  * { margin: 0; padding: 0; box-sizing: border-box; }
  html, body {
    width: 1200px;
    height: 1200px;
    overflow: hidden;
    background: var(--backdrop);
  }
  .spread {
    position: absolute;
    top: 200px;
    left: 60px;
    display: flex;
    gap: 40px;
  }
  .cover {
    width: 520px;
    height: 800px;
    background: var(--teal);
    position: relative;
    overflow: hidden;
    box-shadow: 0 10px 30px var(--shadow);
    color: var(--cream);
  }
  .front-photo {
    height: 420px;
    background: linear-gradient(180deg, var(--photo-glow) 0%, var(--photo-warm) 45%, var(--photo-sea) 80%, #7f7776 100%);
  }
  .front-title {
    font-family: "Marcellus", serif;
    font-weight: 400;
    text-align: center;
    text-transform: uppercase;
    margin-top: 40px;
    line-height: 1.1;
  }
  .front-title .main { font-size: 42px; letter-spacing: 1px; display: block; }
  .front-title .joiner { font-size: 26px; display: block; margin: 6px 0 2px; }
  .front-title .subject { font-size: 38px; display: block; letter-spacing: 1px; }
  .flower-mark { display: block; margin: 24px auto 4px; }
  .front-tagline {
    font-family: "Sacramento", cursive;
    font-size: 38px;
    text-align: center;
    line-height: 1.15;
    padding: 0 50px;
  }
  .back-content {
    padding: 52px 48px 0;
    text-align: center;
  }
  .back-heading {
    font-family: "Marcellus", serif;
    font-weight: 400;
    font-size: 21px;
    line-height: 1.3;
    text-transform: uppercase;
    letter-spacing: 0.5px;
    margin-bottom: 24px;
  }
  .back-copy {
    font-family: "Sacramento", cursive;
    font-size: 23px;
    line-height: 1.3;
    margin-bottom: 18px;
  }
  .back-photo {
    position: absolute;
    left: 0; right: 0; bottom: 0;
    height: 150px;
    background: linear-gradient(160deg, #8f8a86 0%, var(--photo-glow) 35%, var(--sand) 70%, #b88568 100%);
  }
  .back-photo .flower-mark {
    position: absolute;
    left: 50%;
    top: 105px;
    margin: 0 0 0 -9px;
  }
</style>
</head>
<body>
  <main class="spread">
    <section class="cover cover-front">
      <div class="front-photo" role="img" aria-label="Foto: Freundinnen tanzen Hand in Hand im Kreis am Strand bei Sonnenuntergang"></div>
      <h1 class="front-title">
        <span class="main">Das kleine</span>
        <span class="main">Mutproben-Buch</span>
        <span class="joiner">für</span>
        <span class="subject">beste Freundinnen</span>
      </h1>
      <svg class="flower-mark" width="18" height="18" viewBox="0 0 18 18" aria-hidden="true">
        <circle cx="9" cy="9" r="8" fill="var(--cream)"/>
      </svg>
      <p class="front-tagline">Gemeinsam staunen, träumen und Neues wagen</p>
    </section>

    <section class="cover cover-back">
      <div class="back-content">
        <h2 class="back-heading">Raus aus der Routine:<br>Erlebt das Glück<br>geteilter Momente</h2>
        <p class="back-copy">Das Mutproben-Buch für beste Freundinnen schenkt euch 52 bunte Ideen, die euch durch ein Jahr voller Lachen, Neugier und kleiner Wagnisse begleiten. Ein Jahr, das eure Verbindung Woche für Woche tiefer macht.</p>
        <p class="back-copy">Von Ausflügen ins Grüne bis hin zu kreativen Bastelabenden – jede Woche wartet eine neue Aufgabe, die frischen Schwung in euren Alltag bringt. Feiert eure Freundschaft, probiert Neues aus und genießt jede Stunde miteinander.</p>
        <p class="back-copy">Findet heraus, wie viel Freude entsteht, wenn ihr Neues gemeinsam wagt. Macht jede Woche zu einem Erlebnis – mit dem Mutproben-Buch für beste Freundinnen!</p>
      </div>
      <div class="back-photo" role="img" aria-label="Foto: Welle am Sandstrand im warmen Abendlicht">
        <svg class="flower-mark" width="18" height="18" viewBox="0 0 18 18" aria-hidden="true">
          <circle cx="9" cy="9" r="8" fill="var(--cream)"/>
        </svg>
      </div>
    </section>
  </main>
</body>
</html>
```